Facelift for a tiny Ice Cream and Coffee shop website, etc

Revamp of website to be mobile friendly. It is an Ice Cream and Coffee shop entering a very interesting time of Social Distance and what. I like fun, quirky and offbeat. My theme is 60's, Hawaiian, Surf, just for the fun of it.
also would like a design for business cards, rack cards and to-go menus
Updates

I was hoping to see some really original off beat submissions. Most of the submissions so far look the same as what I have, just rearranged.

I am looking for a design that is "out there", edgy, quirky, unusual, off beat, reflective of our little shop. Outside the box.

Target Market(s)

whomever is Googling "Ice Cream" near me

Contact Information for Business Card

Made on the Farm Ice Cream
from the Milk of Pampered Cows
287 E Tamber Ave
Falls Church, VA 22913
www.PorchBellScoops.example

Number of Pages Required

3 page

Font styles to use
Sans Serif

Colors
6b449b

Requirements
Must have
• Must visit site at PorchBellScoops.example. I want photo with giant pink cone first thing you see. After that I want a pleasing meaningful layout that will get people to visit my shop. The Ice Cream is Made on the farm
Nice to have
• I like my 60's Hawaiian theme, but would be open to Space Age,
Should not have
• Soft serve ice cream

```html
<!DOCTYPE html>
<html lang="en">
<head>
<meta charset="utf-8">
<title>Porch Bell Scoops</title>
<link rel="stylesheet" href="https://fonts.googleapis.com/css2?family=Barlow+Condensed:wght@500;600;700;800&family=Barlow:wght@400;500&display=swap">
<style>
:root{
  --cream:#f1e9d3;
  --cream-dark:#e6dcc0;
  --purple:#5b2c8c;
  --purple-dark:#3f1d66;
  --gold:#c9a91f;
  --ink:#2b2b2b;
  --red:#a40b3c;
  --night:#1e1d1c;
  --white:#ffffff;
}
*{box-sizing:border-box;margin:0;padding:0}
html,body{width:1200px;height:3535px;overflow:hidden}
body{position:relative;background:var(--cream);font-family:"Barlow",sans-serif;color:var(--ink)}
.abs{position:absolute}

/* header */
.contact{display:flex;align-items:center;gap:18px;top:82px}
.contact .icon{width:62px;height:62px;border-radius:50%;background:var(--purple);display:flex;align-items:center;justify-content:center}
.contact p{font-family:"Barlow Condensed",sans-serif;font-weight:500;font-size:27px;line-height:33px;color:#333}
.brand{left:470px;top:70px;width:260px;display:flex;flex-direction:column;align-items:center;gap:10px}
.brand .dot{width:56px;height:56px;border-radius:50%;background:var(--purple)}
.brand span{font-family:"Barlow Condensed",sans-serif;font-weight:700;font-size:34px;color:var(--purple);letter-spacing:.5px}

/* nav */
.ribbon{left:36px;top:228px;width:1128px;height:62px}
.nav{left:124px;top:222px;width:954px;height:53px;background:linear-gradient(var(--purple),var(--purple-dark));display:flex;justify-content:space-around;align-items:center;padding:0 40px;box-shadow:0 4px 8px rgba(0,0,0,.35)}
.nav a{color:var(--white);text-decoration:none;font-size:14px;font-weight:500;letter-spacing:.3px}

/* hero */
.hero{left:90px;top:275px;width:1015px;height:556px;background:radial-gradient(ellipse at 66% 42%,#e07aa0 0,#d0668e 28%,#3a3436 55%,#1a1a1a 100%)}
.hero-box{left:354px;top:474px;width:521px;height:186px;background:rgba(30,28,28,.82);text-align:center}
.hero-box h1{font-family:"Barlow Condensed",sans-serif;font-weight:600;font-size:60px;color:var(--white);margin-top:28px;line-height:66px}
.hero-box p{font-family:"Barlow Condensed",sans-serif;font-weight:500;font-size:25px;color:var(--gold);margin-top:8px}

/* welcome */
.eyebrow{left:0;top:876px;width:1200px;display:flex;justify-content:center;align-items:center;gap:14px}
.eyebrow i{display:block;width:238px;border-top:3px dotted #444}
.eyebrow span{font-family:"Barlow Condensed",sans-serif;font-weight:500;font-size:32px;color:#333}
.title{left:0;width:1200px;text-align:center;font-family:"Barlow Condensed",sans-serif;font-weight:800;color:var(--purple);text-shadow:4px 4px 0 var(--gold)}
.welcome-title{top:924px;font-size:86px}
.intro{left:111px;top:1080px;width:452px;font-size:13.5px;line-height:26.6px;color:#333}
.intro p+p{margin-top:26px}
.btn{left:111px;top:1400px;width:135px;height:47px;background:var(--purple);color:var(--white);font-family:"Barlow Condensed",sans-serif;font-weight:600;font-size:19px;display:flex;align-items:center;justify-content:center;box-shadow:4px 4px 0 var(--gold)}
.shop-photo{left:596px;top:1061px;width:491px;height:372px;border:10px solid #b9a2c7;background:linear-gradient(135deg,#8a6d55,#c9b8a0 45%,#e8e6e2 70%,#6d5a4a)}

/* flavors */
.flavors{left:0;top:1532px;width:1200px;height:615px;background:var(--purple)}
.flavors-title{left:0;top:1580px;width:1200px;text-align:center;font-family:"Barlow Condensed",sans-serif;font-weight:800;font-size:76px;color:var(--gold);text-shadow:3px 3px 0 rgba(0,0,0,.35)}
.flavor{border-radius:50%;border:12px solid #e8e0ee;box-shadow:0 6px 16px rgba(0,0,0,.4)}
.flavor.active{border:14px solid var(--gold);display:flex;flex-direction:column;align-items:center;justify-content:center;gap:10px}
.flavor.active span{font-family:"Barlow Condensed",sans-serif;font-weight:600;font-size:30px;color:var(--white)}
.flavor-label{font-family:"Barlow Condensed",sans-serif;font-weight:600;font-size:22px;color:var(--white);transform:translateX(-50%);white-space:nowrap}
.dots{left:577px;top:2115px;display:flex;gap:10px}
.dots i{width:8px;height:8px;border-radius:50%;background:var(--white)}
.dots i.on{background:var(--gold)}

/* gallery */
.gallery-title{top:2205px;font-size:78px}
.stars{left:364px;top:2296px;width:472px;display:flex;align-items:center;gap:10px}
.stars i{flex:1;border-top:1.5px solid var(--purple)}
.g{position:absolute}

/* story */
.footer{left:0;top:3000px;width:1200px;height:535px;background:var(--night)}
.story{left:82px;top:2870px;width:1037px;height:226px;background:var(--red)}
.story h2{position:absolute;left:52px;top:62px;font-family:"Barlow Condensed",sans-serif;font-weight:700;font-size:64px;color:var(--white);text-shadow:3px 3px 0 var(--gold)}
.story p{position:absolute;left:391px;top:60px;width:600px;color:var(--white);font-size:15.5px;line-height:32px}

/* footer */
.foot-brand{left:114px;top:3180px;display:flex;align-items:center;gap:12px}
.foot-brand .dot{width:44px;height:44px;border-radius:50%;background:var(--purple)}
.foot-brand span{font-family:"Barlow Condensed",sans-serif;font-weight:700;font-size:30px;color:var(--white)}
.col h3{font-family:"Barlow Condensed",sans-serif;font-weight:600;font-size:33px;color:var(--white);margin-bottom:16px;line-height:36px}
.col li{list-style:none;color:var(--white);font-size:13.5px;line-height:31.6px}
.hours li{display:flex}
.hours li b{font-weight:400;width:111px}
.rule{left:114px;top:3456px;width:972px;border-top:1px solid #444}
.copyright{left:0;top:3482px;width:1200px;text-align:center;color:#ddd;font-size:15px}
</style>
</head>
<body>

<div class="contact abs" style="left:113px">
  <div class="icon"><svg width="24" height="24" viewBox="0 0 24 24"><path fill="#fff" d="M6.6 10.8a15 15 0 0 0 6.6 6.6l2.2-2.2c.3-.3.7-.4 1-.2 1.1.4 2.3.6 3.6.6.6 0 1 .4 1 1V20c0 .6-.4 1-1 1A17 17 0 0 1 3 4c0-.6.4-1 1-1h3.5c.6 0 1 .4 1 1 0 1.3.2 2.5.6 3.6.1.3 0 .7-.2 1z"/></svg></div>
  <p>287 E TAMBER AVE<br>FALLS CHURCH, VA 22913</p>
</div>

<div class="brand abs"><div class="dot"></div><span>PORCH BELL SCOOPS</span></div>

<div class="contact abs" style="left:764px">
  <div class="icon"><svg width="24" height="24" viewBox="0 0 24 24"><path fill="#fff" d="M6.6 10.8a15 15 0 0 0 6.6 6.6l2.2-2.2c.3-.3.7-.4 1-.2 1.1.4 2.3.6 3.6.6.6 0 1 .4 1 1V20c0 .6-.4 1-1 1A17 17 0 0 1 3 4c0-.6.4-1 1-1h3.5c.6 0 1 .4 1 1 0 1.3.2 2.5.6 3.6.1.3 0 .7-.2 1z"/></svg></div>
  <p>CALL US : 703 555-0148</p>
</div>

<svg class="ribbon abs" viewBox="0 0 1128 62" aria-hidden="true">
  <polygon points="0,10 100,0 100,52 20,58 40,32" fill="#4a2275"/>
  <polygon points="1128,10 1028,0 1028,52 1108,58 1088,32" fill="#4a2275"/>
</svg>
<nav class="nav abs">
  <a>HOME</a><a>ICE CREAM</a><a>COFFEE &amp; ESPRESSO</a><a>SMOOTHIES</a><a>GIFT CARDS</a><a>MAGNETS</a><a>MUGS</a><a>T SHIRTS</a>
</nav>

<div class="hero abs" role="img" aria-label="Giant pink ice cream cone in front of a black and white cinema crowd wearing 3D glasses"></div>
<div class="hero-box abs">
  <h1>PORCH BELL SCOOPS</h1>
  <p>SED UT PERSPICIATIS UNDE OMNIS ISTE NATUS ERROR</p>
</div>

<div class="eyebrow abs"><i></i><span>WELCOME TO</span><i></i></div>
<h2 class="title welcome-title abs">PORCH BELL SCOOPS</h2>

<div class="intro abs">
  <p>We feature Farm Made Ice Cream from Hollow Brook Dairy.</p>
  <p>They make Ice Cream from the milk of their Uber-pampered Grass Fed Jersey Cows. The result is a super smooth, ultra-creamy, but not overly sweet Ice Cream.Our shop is very tiny and at the current time there is no indoor seating, but plenty of outside options and a nice canopy in case the weather gets wet.</p>
  <p>To abide by Social Distancing guidelines, we have configured the shop so that there is only enough room inside for one party at a time Everything on the Menu is available, just come on in..</p>
</div>
<div class="btn abs">READ MORE</div>
<div class="shop-photo abs" role="img" aria-label="Inside the shop: shelves of collectible figurines above the ice cream counter"></div>

<section class="flavors abs"></section>
<h2 class="flavors-title abs">OUR FLAVORS</h2>
<div class="flavor abs" style="left:101px;top:1778px;width:194px;height:194px;background:radial-gradient(#e9ece8,#6e7c86)" role="img" aria-label="Scoop of chocolate chip ice cream in a cone"></div>
<div class="flavor abs" style="left:241px;top:1755px;width:240px;height:240px;background:radial-gradient(#d9a0a6,#8a5a36)" role="img" aria-label="Ice cream cookie sandwiches"></div>
<div class="flavor abs" style="left:716px;top:1755px;width:240px;height:240px;background:radial-gradient(#f3ede4,#3a2c2a)" role="img" aria-label="Brownie sundae with chocolate sauce"></div>
<div class="flavor abs" style="left:903px;top:1778px;width:194px;height:194px;background:radial-gradient(#e7c0b8,#8a2b2e)" role="img" aria-label="Cafe glace in a paper coffee cup"></div>
<div class="flavor active abs" style="left:448px;top:1723px;width:304px;height:304px;background:radial-gradient(#8a6240,#2a1d16)" role="img" aria-label="Root beer float in a glass mug">
  <span>ROOT BEER FLOAT</span>
  <svg width="26" height="26" viewBox="0 0 26 26"><circle cx="13" cy="13" r="13" fill="#fff"/><path d="M7 10l6 6 6-6" stroke="#333" stroke-width="3" fill="none"/></svg>
</div>
<span class="flavor-label abs" style="left:202px;top:2015px">CUP OR CONE</span>
<span class="flavor-label abs" style="left:376px;top:2055px">FROSTY CRUNCHER</span>
<span class="flavor-label abs" style="left:820px;top:2055px">BROWNIE SUNDAE</span>
<span class="flavor-label abs" style="left:995px;top:2015px">CAFE GLACE</span>
<div class="dots abs"><i></i><i class="on"></i><i></i></div>

<h2 class="title gallery-title abs">PHOTO GALLERY</h2>
<div class="stars abs"><i></i>
  <svg width="84" height="14" viewBox="0 0 84 14" aria-hidden="true"><g fill="#5b2c8c"><path id="s" d="M7 0l2 5h5l-4 3 2 5-5-3-5 3 2-5-4-3h5z"/><use href="#s" x="17"/><use href="#s" x="34"/><use href="#s" x="51"/><use href="#s" x="68"/></g></svg>
<i></i></div>
<div class="g" style="left:111px;top:2363px;width:478px;height:203px;background:linear-gradient(135deg,#9a7b5a,#d8cfc2 50%,#5a4636)" role="img" aria-label="Shop counter with menu boards and figurine shelves"></div>
<div class="g" style="left:610px;top:2363px;width:228px;height:428px;background:linear-gradient(160deg,#b33a3a,#d9c7bf 40%,#e79ab2 55%,#2a2a2a)" role="img" aria-label="Man holding up a pink ice cream cone"></div>
<div class="g" style="left:858px;top:2363px;width:228px;height:203px;background:linear-gradient(135deg,#6a5a4e,#c7a48a 50%,#3b3a44)" role="img" aria-label="Shelves of colorful collectible figurines"></div>
<div class="g" style="left:111px;top:2588px;width:230px;height:203px;background:linear-gradient(160deg,#3a4b6a,#e87a2a 55%,#b85a1a)" role="img" aria-label="Orange smoothie in a cup"></div>
<div class="g" style="left:360px;top:2588px;width:229px;height:203px;background:linear-gradient(160deg,#2a2a2a,#f0ece6 45%,#8a2a1e)" role="img" aria-label="Coffee topped with whipped cream and chocolate drizzle"></div>
<div class="g" style="left:858px;top:2588px;width:228px;height:203px;background:linear-gradient(135deg,#5a4434,#d8d0c8 55%,#8a6a4e)" role="img" aria-label="Ice cream display freezer behind the counter"></div>

<footer class="footer abs"></footer>
<div class="story abs">
  <h2>OUR STORY }</h2>
  <p>To abide by Social Distancing guidelines, we have configured the shop so that there is only enough room inside for one party at a time, verything on the Menu is available, just come on in.</p>
</div>

<div class="foot-brand abs"><div class="dot"></div><span>PORCH BELL SCOOPS</span></div>

<div class="col hours abs" style="left:398px;top:3141px;width:240px">
  <h3>HOURS</h3>
  <ul>
    <li><b>MON</b>CLOSED</li><li><b>TUES</b>CLOSED</li><li><b>WED</b>CLOSED</li><li><b>THURS</b>CLOSED</li>
    <li><b>FRI</b>2 PM - 8 PM</li><li><b>SAT</b>11 AM - 8 PM</li><li><b>SUN</b>11 AM - 6 PM</li>
  </ul>
</div>
<div class="col abs" style="left:682px;top:3141px">
  <h3>LINKS</h3>
  <ul><li>HOME</li><li>ICE CREAM</li><li>COFFEE &amp; ESPRESSO</li><li>SMOOTHIES</li><li>GIFT CARDS</li><li>MAGNETS</li><li>MUGS</li><li>T SHIRTS</li></ul>
</div>
<div class="col abs" style="left:898px;top:3141px">
  <h3>ADDRESS</h3>
  <ul><li>287 E TAMBER AVE</li><li>FALLS CHURCH, VA 22913</li><li>TEXT -703 555-0148</li></ul>
</div>
<div class="rule abs"></div>
<p class="copyright abs">© 2020 Copy Porch Bell Scoops.all Rights Reserved</p>

</body>
</html>
```